PEACFUL ACUPUNCTURE PRACTITIONER NEEDS A NEW COAT

I need a new design for an exiting website http://willowgateneedlework.com/ for a acupuncturist. This will be a minimalism design with lots and lots of white space. Home page and one interior page. Please keep the feeling of calm and peaceful serenity. For Color scheme: https://www.morningfernclinic.com/fertility. The bottom part of the home page with sections and links to the service pages: https://harborlotuswellness.com/. The client likes this the best: http://mfclinic.com/. I'm attaching the logo and content pages.

Target Market(s)

Women

Industry/Entity Type

Wellness, health, wellbeing, meditation

Number of Pages Required

2 page

Font styles to use
Sans Serif
Decorative

Colors

Designer to choose colors to be used in the design.

Requirements
Must have
Nice to have
• Follow new website drafts and links
Should not have
• Busy with bright colors. No poping

```html
<!DOCTYPE html>
<html lang="en">
<head>
<meta charset="utf-8">
<title>Willowgate Acupuncture – Website Pages</title>
<link href="https://fonts.googleapis.com/css2?family=Titillium+Web:wght@400;600&display=swap" rel="stylesheet">
<style>
:root{
  --board:#1f1a17;
  --page:#ffffff;
  --nav:#dde3e2;
  --nav-store:#efe6cf;
  --ink:#2a2a2a;
  --muted:#555;
  --footer:#5e8a82;
  --footer-store:#c08a35;
  --panel:#dde3e2;
  --thumb:#c6c7ca;
  --button:#111;
  --star:#d8383a;
  --accent:#d98a8f;
}
*{box-sizing:border-box;margin:0;padding:0}
html,body{width:1200px;height:780px;overflow:hidden}
body{background:var(--board);font-family:"Titillium Web",sans-serif;color:var(--ink);position:relative}
.page{position:absolute;top:42px;width:214px;background:var(--page);overflow:hidden}
.abs{position:absolute}
/* nav */
.nav{position:absolute;left:0;top:0;width:100%;height:11px;background:var(--nav)}
.nav.store{background:var(--nav-store)}
.logo{position:absolute;left:45px;top:3px;display:flex;align-items:center;gap:2px;font-size:4px;line-height:5px;color:#6b6b6b}
.logo .mark{width:4px;height:4px;border-radius:50%;background:var(--accent)}
.nav-links{position:absolute;left:98px;top:4px;display:flex;gap:3px;font-size:2.1px;line-height:3px;color:#444;text-transform:uppercase}
.nav-links .current{color:#aaa}
/* hero */
.hero{position:absolute;left:0;top:11px;width:100%;height:48px;color:#fff;text-align:center}
.hero-sage{background:linear-gradient(100deg,#4f615b,#7f9187 55%,#5d6f68)}
.hero-amber{background:linear-gradient(100deg,#6e4f22,#a9823f 55%,#7e5b27)}
.hero-fern{background:linear-gradient(100deg,#5d7a55,#93ab7f 55%,#6b8a60)}
.hero-olive{background:linear-gradient(100deg,#6f6a2e,#9b8a3e 55%,#7a6b2c)}
.hero-slate{background:linear-gradient(100deg,#474e62,#7a8094 55%,#555c70)}
.hero h1{font-weight:400;font-size:5px;line-height:6px;letter-spacing:.1px}
.btn{display:inline-block;background:var(--button);color:#fff;font-weight:600;font-size:2.6px;line-height:6px;padding:0 4px;text-transform:uppercase}
.btn.light{background:#fff;color:#111}
/* body text */
h2.section{font-weight:400;font-size:5px;line-height:6px;text-align:center;color:#111}
h3{font-weight:400;font-size:3px;line-height:4px;color:#222}
h4{font-weight:400;font-size:2.4px;line-height:3.3px;color:#222;text-transform:uppercase}
p,li{font-size:1.9px;line-height:3.3px;color:var(--muted)}
ul{list-style:none}
li::before{content:"• "}
.thumb{width:30px;height:30px;background:var(--thumb)}
.photo{width:30px;height:30px}
.chev{position:absolute;left:165px;width:4px;height:3px}
/* footer */
.footer{position:absolute;left:0;bottom:0;width:100%;height:59px;background:var(--footer);color:#fff}
.footer.store{background:var(--footer-store);height:40px}
.footer ul.links li,.footer .contact p{font-size:2.3px;line-height:6.6px;color:#fff}
.footer ul.links li::before{content:none}
.footer .links{position:absolute;left:45px;top:6px}
.footer .contact{position:absolute;left:76px;top:6px}
.footer .social{position:absolute;left:77px;top:45px;display:flex;gap:3px}
.footer .social span{width:3px;height:3px;border-radius:50%;background:#fff}
.footer .brand{position:absolute;left:138px;top:24px;width:34px;text-align:center}
.footer .brand .mark{width:9px;height:9px;border-radius:50%;background:var(--accent);margin:0 auto 1px}
.footer .brand .name{font-size:4px;line-height:5px;color:#fff}
.footer .copy{position:absolute;right:44px;top:47px;font-size:1.5px;line-height:2px;color:#fff}
/* forms */
.field{position:absolute;height:5px;border:0.3px solid #cfd3d3;font-size:1.8px;line-height:4.5px;color:#aaa;padding-left:1px}
</style>
</head>
<body>

<!-- Home -->
<section class="page" style="left:37px;height:270px">
  <header class="nav">
    <div class="logo"><span class="mark"></span>Willowgate</div>
    <nav class="nav-links"><span>Treatments ˅</span><span class="current">Home</span><span>About</span><span>Testimonials</span><span>Contact/Book</span><span>Shop</span></nav>
  </header>
  <div class="hero hero-sage" role="img" aria-label="Soft photo of a calm treatment room">
    <div class="abs" style="left:44px;top:3px;width:126px">
      <h3 style="color:#fff">Philosophy of Care</h3>
      <p style="color:#fff;font-size:2.1px;line-height:4.9px">Acupuncture &amp; Chinese Herbal Medicine are rooted in over 3000 years of history and tradition. As a complete medical system that has remained flexible and relevant we honor what has worked from the past while embracing the medicine of tomorrow. At Willowgate Acupuncture we provide compassionate, respectful and empowering care in a safe and inclusive environment. Our goal is to harmonize physical, mental and emotional wellbeing to strengthen the point from which we all strive to live.</p>
      <span class="btn light" style="margin-top:2px">Book Now</span>
    </div>
  </div>
  <h2 class="section abs" style="left:0;width:100%;top:64px">TREATMENTS</h2>
  <div class="abs" style="left:45px;top:72px;display:flex;gap:2px">
    <div style="width:29.7px;text-align:center"><div class="photo" style="background:linear-gradient(135deg,#8a9a5a,#c8c9a8)" role="img" aria-label="Bird nest with eggs"></div><h4 style="font-size:1.7px;margin-top:1px">Fertility &amp; Pregnancy</h4></div>
    <div style="width:29.7px;text-align:center"><div class="photo" style="background:linear-gradient(135deg,#d96a7a,#d8d6d0)" role="img" aria-label="Stones and flower petals"></div><h4 style="font-size:1.7px;margin-top:1px">Hormone Balance</h4></div>
    <div style="width:29.7px;text-align:center"><div class="photo" style="background:linear-gradient(135deg,#6e8a4e,#a8b88f)" role="img" aria-label="Tree canopy seen from below"></div><h4 style="font-size:1.7px;margin-top:1px">Strength &amp; Structure</h4></div>
    <div style="width:29.7px;text-align:center"><div class="photo" style="background:linear-gradient(135deg,#6a6a86,#c9a7a8)" role="img" aria-label="Hands holding a small heart"></div><h4 style="font-size:1.7px;margin-top:1px">Emotional Wellbeing</h4></div>
  </div>
  <div class="abs" style="left:45px;top:113px;width:124px;height:84px;background:var(--panel)">
    <div class="abs" style="left:31px;top:4px;width:62px">
      <div style="color:var(--star);font-size:4px;line-height:4px;letter-spacing:.3px">★★★★★</div>
      <h3 style="font-size:2.4px;line-height:3.4px">Lena P.</h3>
      <p style="font-size:1.6px;line-height:2.6px;color:#333">Elm Hollow, NY</p>
      <p style="font-size:1.6px;line-height:3.1px;margin-top:3px">I went to Willowgate as my very first experience with acupuncture, so I was nervous about the needles. Maren was kind and professional and clearly explained everything and what I might feel when the pins go in. It was truly relaxing and calming. I felt the energy moving and healing going on. I would highly recommend Willowgate, and Maren has great knowledge of Chinese medicine and herbs. I appreciate that she has a sliding scale so care is more affordable than a regular basis.</p>
    </div>
    <span class="btn abs" style="left:41px;top:73px">More Testimonials</span>
  </div>
  <footer class="footer">
    <ul class="links"><li>About</li><li>Fertility &amp; Pregnancy</li><li>Hormone Balance</li><li>Strength &amp; Structure</li><li>Emotional Wellbeing</li><li>Online Shop</li><li>Testimonials</li></ul>
    <div class="contact"><p>Contact:</p><p>555-014-2290</p><p>info@willowgate.com</p></div>
    <div class="social"><span></span><span></span><span></span><span></span></div>
    <div class="brand"><div class="mark"></div><div class="name">Willowgate</div></div>
    <p class="copy">Copyright @ 2021 Willowgate All Rights Reserved</p>
  </footer>
</section>

<!-- About -->
<section class="page" style="left:265px;height:696px">
  <header class="nav">
    <div class="logo"><span class="mark"></span>Willowgate</div>
    <nav class="nav-links"><span>Treatments ˅</span><span>Home</span><span class="current">About</span><span>Testimonials</span><span>Contact/Book</span><span>Shop</span></nav>
  </header>
  <div class="hero hero-amber" role="img" aria-label="Warm photo of acupuncture treatment">
    <h1 style="padding-top:19px">ABOUT WILLOWGATE</h1>
  </div>

  <article class="abs" style="left:45px;top:63px;width:124px">
    <div class="thumb"></div>
    <h3 style="margin-top:6px">About Maren</h3>
    <p style="margin-top:2px">Maren Oakes is a licensed acupuncturist and herbalist as well as nationally certified in acupuncture and herbal medicine. She obtained her masters degree and has studied at an integrated hospital abroad. She worked for an herb company, a leader of high quality lab tested formulas, as a consultant to both acupuncturists and western MDs. Every year she commits to attending classes to practice better care.</p>
    <h3 style="margin-top:4px;font-size:2.4px">Area of focus:</h3>
    <p>"I have focused on hormonal health and fertility through bodywork, acupuncture and herbal medicine for decades. A fascination with how the hormonal feedback loops of our bodies can be accessed through the patterns of acupuncture led me towards fertility and conception. I began my training with a mentor and then further study abroad. In my free time I love hiking, camping, reading, eating vegetables, sitting quietly, feeding the birds while sipping teas, laughing at good jokes and enjoying time with my animal friends."</p>
  </article>
  <svg class="chev" style="top:169px" viewBox="0 0 4 3"><path d="M0.5 2.5 L2 1 L3.5 2.5" fill="none" stroke="#333" stroke-width=".4"/></svg>

  <article class="abs" style="left:45px;top:178px;width:124px">
    <div class="thumb"></div>
    <h3 style="margin-top:6px">About Dogtor Pip</h3>
    <p style="margin-top:2px">Pip came up from the south in July. After some (ahem) training she began practicing and is currently in charge of operations (not really). She prefers chin scratches to head scratches and has never met a treat she didn't like. She never enters treatment rooms and air filters are constantly on.</p>
  </article>
  <svg class="chev" style="top:234px" viewBox="0 0 4 3"><path d="M0.5 2.5 L2 1 L3.5 2.5" fill="none" stroke="#333" stroke-width=".4"/></svg>

  <article class="abs" style="left:45px;top:243px;width:124px">
    <div class="thumb"></div>
    <h3 style="margin-top:6px">About the Clinic:</h3>
    <p style="margin-top:2px">Willowgate Acupuncture is a small clinic off the beaten path downtown. Treatments take place in a private, relaxed and quiet setting. Private, non metered parking is available right outside the door.</p>
    <h3 style="margin-top:3px;font-size:2.4px">Non-discrimination policy:</h3>
    <p>Willowgate does not discriminate on the basis of race or national origin, age, religion, ability, education, height, weight, body type, marital status, sexual orientation, sex, or gender identity. All are welcome.</p>
    <h3 style="margin-top:3px;font-size:2.4px">Accessibility:</h3>
    <p>A carpeted stairs with railing. Unfortunately, no elevator or ramp. Gender inclusive restroom.</p>
  </article>
  <svg class="chev" style="top:324px" viewBox="0 0 4 3"><path d="M0.5 2.5 L2 1 L3.5 2.5" fill="none" stroke="#333" stroke-width=".4"/></svg>

  <article class="abs" style="left:45px;top:335px;width:124px">
    <div class="thumb"></div>
    <h3 style="margin-top:5px">About Acupuncture:</h3>
    <p>Acupuncture is the insertion of thin needles at specific points which act as guideposts for healing. These guideposts help the body use its own mechanisms for self regulation to restore health. The needles used are sterile, disposable and as thin as a cat's whisker. Often they create a slight tingling sensation, allowing the qi or energy to travel through the channels, mending areas of disharmony.</p>
  </article>
  <svg class="chev" style="top:389px" viewBox="0 0 4 3"><path d="M0.5 2.5 L2 1 L3.5 2.5" fill="none" stroke="#333" stroke-width=".4"/></svg>

  <article class="abs" style="left:45px;top:399px;width:124px">
    <div class="thumb"></div>
    <h3 style="margin-top:5px">About Herbs:</h3>
    <p>Herbal formulas aid in extending and enhancing acupuncture treatments. Daily use acts as a reinforcing agent, encouraging the body towards a healthier path until it is strong enough to take over on its own. Herbs rarely have side effects and can be taken as a tea, tablet or tincture. All herbal formulas used here have passed stringent lab analysis for purity and heavy metals.</p>
    <span class="btn" style="margin-top:4px">Shop Now</span>
  </article>
  <svg class="chev" style="top:453px" viewBox="0 0 4 3"><path d="M0.5 2.5 L2 1 L3.5 2.5" fill="none" stroke="#333" stroke-width=".4"/></svg>

  <article class="abs" style="left:45px;top:478px;width:124px">
    <div class="thumb"></div>
    <h3 style="margin-top:6px">FAQ Frequently asked questions:</h3>
    <h4 style="margin-top:2px;font-size:1.9px">How do I know if acupuncture can help me?</h4>
    <p>Acupuncture has been helping patients for over 3,000 years and it can help you too! The goal of the initial consultation is to fully comprehend your personal health goals and history. From there, we establish a treatment plan that is effective while being time and cost efficient.</p>
    <h4 style="margin-top:2.5px;font-size:1.9px">Does acupuncture hurt?</h4>
    <p>Needles can create a slight tingling sensation at the area of insertion but rarely is there ever any pain.</p>
    <h4 style="margin-top:2.5px;font-size:1.9px">How big are the needles and are they sterile?</h4>
    <p>Needles range in diameter and length depending on the area of the body being treated. Most are about as wide as a cat's whisker. Every needle is single use.</p>
    <h4 style="margin-top:2.5px;font-size:1.9px">What are treatments like and how long do they take?</h4>
    <p>Treatments include a time for discussion followed by needle insertion, then usually about 30 minutes of quiet rest with the needles in place.</p>
    <h4 style="margin-top:2.5px;font-size:1.9px">How many treatments will I need?</h4>
    <p>Treatment plans are individual and are often influenced by factors like the depth of disease. In general, patients should be seen at least once a week until a solid foundation of health is created.</p>
    <h4 style="margin-top:2.5px;font-size:1.9px">How much does it cost?</h4>
    <p>Although insurance is not accepted, a sliding scale is offered to make treatments as affordable as possible. Please reach out for current scale limits.</p>
  </article>
  <svg class="chev" style="top:626px" viewBox="0 0 4 3"><path d="M0.5 2.5 L2 1 L3.5 2.5" fill="none" stroke="#333" stroke-width=".4"/></svg>

  <footer class="footer">
    <ul class="links"><li>About</li><li>Fertility &amp; Pregnancy</li><li>Hormone Balance</li><li>Strength &amp; Structure</li><li>Emotional Wellbeing</li><li>Online Shop</li><li>Testimonials</li></ul>
    <div class="contact"><p>Contact:</p><p>555-014-2290</p><p>info@willowgate.com</p></div>
    <div class="social"><span></span><span></span><span></span><span></span></div>
    <div class="brand"><div class="mark"></div><div class="name">Willowgate</div></div>
    <p class="copy">Copyright @ 2021 Willowgate All Rights Reserved</p>
  </footer>
</section>

<!-- Treatment: Fertility & Pregnancy -->
<section class="page" style="left:493px;height:442px">
  <header class="nav">
    <div class="logo"><span class="mark"></span>Willowgate</div>
    <nav class="nav-links"><span>Treatments ˅</span><span>Home</span><span>About</span><span>Testimonials</span><span>Contact/Book</span><span>Shop</span></nav>
  </header>
  <div class="hero hero-fern" role="img" aria-label="Green foliage and blossoms">
    <h1 style="padding-top:15px">TREATMENTS</h1>
    <h1 style="margin-top:4px">FERTILITY &amp; PREGNANCY</h1>
  </div>
  <div class="photo abs" style="left:45px;top:63px;background:linear-gradient(135deg,#7f9550,#c9c8a4)" role="img" aria-label="Bird nest with eggs"></div>
  <h3 class="abs" style="left:45px;top:99px">FERTILITY</h3>
  <p class="abs" style="left:45px;top:106px;width:126px">Whether you are attempting to conceive at home or with the help of assisted reproductive technologies like IVF or IUI, fertility challenges can feel isolating and overwhelming. Emotional strains, financial concerns and often a diagnosis of "unexplained infertility" can leave families feeling powerless. Our goal is to help achieve pregnancy while creating a healing space of support and individualized care.</p>
  <div class="abs" style="left:45px;top:128px;width:126px">
    <h3 style="font-size:2.4px">Conception at home/ICI:</h3>
    <p>Difficulties tracking your cycle or repeated unsuccessful conception attempts are often unexpected. Taking the time to understand your unique menstrual cycle can be the key to fertility. By preparing your body for pregnancy you can improve your chance of a healthy pregnancy and lessen your risk for complications.</p>
  </div>
  <div class="abs" style="left:45px;top:152px;width:126px">
    <h3 style="font-size:2.4px">IUI and IVF:</h3>
    <p>Recent studies confirm Traditional Chinese Medicine's positive influence on achieving pregnancy in concert with Assisted Reproductive therapies. Often a diagnosis of infertility can be stressful enough, but compounded by complex pharmaceutical regimens and multiple doctors appointments can leave families overwhelmed. Acupuncture provides a safe, healing space to process and recover. Patients who received acupuncture on transfer day improved their conception rates.</p>
  </div>
  <div class="abs" style="left:45px;top:180px;width:126px">
    <h4 style="font-size:2.1px">Acupuncture can help:</h4>
    <ul>
      <li>mitigate complications from irregular menses and PCOS or Endometriosis</li>
      <li>encourage implantation, embryo growth and prevent miscarriage</li>
      <li>counter negative stress feedback loops that affect hormone balance</li>
      <li>improve follicle count and quality</li>
      <li>increase uterine lining thickness</li>
      <li>promote health for advanced parental age concerns</li>
      <li>lower elevated FSH</li>
      <li>decrease inflammation for PID or fallopian tube factors</li>
      <li>help to calm autoimmune disorders</li>
      <li>address sperm factor issues</li>
      <li>improve success rates of ICI, IUI and IVF</li>
      <li>help prepare a solid foundation for donor sperm or donor egg cycles</li>
      <li>support for single mothers and parents by choice and surrogates</li>
      <li>help heal mild to moderate OHSS</li>
    </ul>
  </div>
  <h3 class="abs" style="left:45px;top:245px">PREGNANCY, LABOR &amp; DELIVERY, POSTPARTUM CARE</h3>
  <div class="abs" style="left:45px;top:253px;width:126px">
    <h3 style="font-size:2.4px">Pregnancy:</h3>
    <p>Just as every person is unique so too is every pregnancy. The experience and resulting transformation is deeply personal and should be celebrated in health and happiness. Sometimes this transformation can strain the physical body, leading to discomfort or complications. Through acupuncture we work to prevent that stress from ever beginning. During pregnancy, treatments optimize fetal growth and encourage balance and strength for the parent to be. Labor preparation treatments in the time surrounding labor focus on proper fetal position and a smooth and timely labor so induction can be avoided.</p>
  </div>
  <div class="abs" style="left:45px;top:296px;width:126px">
    <h3 style="font-size:2.4px">Postpartum care:</h3>
    <p>After delivery it is imperative to rebuild and rebalance. The instinct is to nest and nurture but by taking care of ones own body one can better care for those at home. Acupuncture treatments focus on relaxation, restoration and creating renewed stores of energy.</p>
  </div>
  <div class="abs" style="left:45px;top:318px;width:126px">
    <h4 style="font-size:2.1px">Acupuncture can help:</h4>
    <ul style="line-height:3px">
      <li style="line-height:3px">Stop insomnia or restless sleep</li>
      <li style="line-height:3px">Prevent miscarriage</li>
      <li style="line-height:3px">Alleviate constipation</li>
      <li style="line-height:3px">Ease hemorrhoid discomfort</li>
      <li style="line-height:3px">Improve energy</li>
      <li style="line-height:3px">Soothe low back ache, sciatica &amp; carpal tunnel</li>
      <li style="line-height:3px">Stop heartburn</li>
      <li style="line-height:3px">Reduce edema</li>
      <li style="line-height:3px">Help to control gestational hypertension or diabetes</li>
      <li style="line-height:3px">Promote timely labor with proper presentation</li>
      <li style="line-height:3px">Postpartum complications like depression or lactation</li>
      <li style="line-height:3px">Prevent or help manage morning sickness</li>
      <li style="line-height:3px;">Improve sensation and shorten healing time for delivery tears</li>
    </ul>
  </div>
  <footer class="footer">
    <ul class="links"><li>About</li><li>Fertility &amp; Pregnancy</li><li>Hormone Balance</li><li>Strength &amp; Structure</li><li>Emotional Wellbeing</li><li>Online Shop</li><li>Testimonials</li></ul>
    <div class="contact"><p>Contact:</p><p>555-014-2290</p><p>info@willowgate.com</p></div>
    <div class="social"><span></span><span></span><span></span><span></span></div>
    <div class="brand"><div class="mark"></div><div class="name">Willowgate</div></div>
    <p class="copy">Copyright @ 2021 Willowgate All Rights Reserved</p>
  </footer>
</section>

<!-- Store -->
<section class="page" style="left:721px;height:208px">
  <header class="nav store">
    <p class="abs" style="left:44px;top:4px;font-size:1.8px;line-height:3px;color:#444">&lt; Back To Main Site</p>
    <div class="logo" style="left:90px"><span class="mark"></span>Willowgate Store</div>
    <p class="abs" style="left:155px;top:4px;font-size:1.8px;line-height:3px;color:#444">CONTACT</p>
    <svg class="abs" style="left:164px;top:3.5px;width:5px;height:4px" viewBox="0 0 10 8"><path d="M0.5 0.8h1.6l1.3 4.6h5l1.1-3.4H3" fill="none" stroke="#444" stroke-width=".8"/><circle cx="4" cy="7" r=".7" fill="#444"/><circle cx="8" cy="7" r=".7" fill="#444"/></svg>
  </header>
  <div class="hero hero-olive" style="text-align:left">
    <div class="abs" style="left:44px;top:0;width:51px;height:48px;background:linear-gradient(160deg,#a9c96a,#4e7a2e)" role="img" aria-label="Glass bottle of herbal tincture among leaves"></div>
    <h1 class="abs" style="left:101px;top:15px">NEW ITEM!</h1>
    <p class="abs" style="left:101px;top:22px;color:#fff;font-size:2.8px">Herb Number 1</p>
    <p class="abs" style="left:101px;top:28px;color:#fff;font-size:2.8px">Only $51.99</p>
  </div>
  <div class="abs" style="left:44px;top:63px;display:grid;grid-template-columns:repeat(4,29.7px);column-gap:2px;row-gap:3px">
    <div><div class="thumb" style="width:29.7px"></div><p style="color:#222">Herb Number 1</p><p style="color:#222">Only $51.99</p></div>
    <div><div class="thumb" style="width:29.7px"></div><p style="color:#222">Herb Number 2</p><p style="color:#222">Only $51.99</p></div>
    <div><div class="thumb" style="width:29.7px"></div><p style="color:#222">Herb Number 3</p><p style="color:#222">Only $51.99</p></div>
    <div><div class="thumb" style="width:29.7px"></div><p style="color:#222">Herb Number 4</p><p style="color:#222">Only $51.99</p></div>
    <div><div class="thumb" style="width:29.7px"></div><p style="color:#222">Herb Number 5</p><p style="color:#222">Only $51.99</p></div>
    <div><div class="thumb" style="width:29.7px"></div><p style="color:#222">Herb Number 6</p><p style="color:#222">Only $51.99</p></div>
    <div><div class="thumb" style="width:29.7px"></div><p style="color:#222">Herb Number 7</p><p style="color:#222">Only $51.99</p></div>
    <div><div class="thumb" style="width:29.7px"></div><p style="color:#222">Herb Number 8</p><p style="color:#222">Only $51.99</p></div>
  </div>
  <p class="abs" style="left:0;width:100%;top:154px;text-align:center;font-size:3px;color:#222">‹ 1 2 3 4 5 ... ›</p>
  <footer class="footer store">
    <div class="abs" style="left:44px;top:6px">
      <p style="color:#fff;font-size:1.9px;line-height:5.4px">CART</p>
      <p style="color:#fff;font-size:1.9px;line-height:5.4px">CONTACT/BOOKING</p>
      <p style="color:#fff;font-size:1.9px;line-height:5.4px">&lt; Back To Main Site</p>
    </div>
    <div class="brand" style="top:6px"><div class="mark"></div><div class="name">Willowgate</div></div>
    <p class="copy" style="top:27px">Copyright @ 2021 Willowgate All Rights Reserved</p>
  </footer>
</section>

<!-- Contact / Booking -->
<section class="page" style="left:949px;height:225px">
  <header class="nav">
    <div class="logo"><span class="mark"></span>Willowgate</div>
    <nav class="nav-links"><span>Treatments ˅</span><span>Home</span><span>About</span><span>Testimonials</span><span class="current">Contact/Book</span><span>Shop</span></nav>
  </header>
  <div class="hero hero-slate" role="img" aria-label="Muted photo of a relaxing treatment">
    <h1 style="padding-top:12px">CONTACT / BOOKING</h1>
    <svg class="abs" style="left:60px;top:22px;width:6px;height:7px" viewBox="0 0 12 14"><path d="M6 13.5S1 8 1 5a5 5 0 0 1 10 0c0 3-5 8.5-5 8.5z" fill="#fff"/><circle cx="6" cy="5" r="1.8" fill="#5e6478"/></svg>
    <svg class="abs" style="left:103px;top:22px;width:6px;height:7px" viewBox="0 0 12 14"><path d="M3 1l2 3-1.4 1.6c.8 2 2 3.3 3.8 4.3L9 8.4l2.6 2-1 2.6C5.8 12.6 1 7.5 1 2.4z" fill="#fff"/></svg>
    <svg class="abs" style="left:145px;top:23px;width:11px;height:6px" viewBox="0 0 22 12"><rect x=".5" y=".5" width="21" height="11" fill="#fff"/><path d="M.5 .5L11 7 21.5 .5" fill="none" stroke="#5e6478" stroke-width=".8"/></svg>
    <p class="abs" style="left:55px;top:31px;color:#fff;font-size:1.8px">Address</p>
    <p class="abs" style="left:97px;top:31px;color:#fff;font-size:1.8px">555-014-2290</p>
    <p class="abs" style="left:136px;top:31px;color:#fff;font-size:1.8px">info@willowgate.com</p>
  </div>
  <div class="field" style="left:44px;top:67px;width:39px">First Name</div>
  <div class="field" style="left:87px;top:67px;width:39px">Last Name</div>
  <div class="field" style="left:44px;top:76px;width:82px">Phone</div>
  <div class="field" style="left:44px;top:85px;width:82px">E-Mail</div>
  <div class="field" style="left:44px;top:93px;width:82px">General Inquiry / Booking (Drop Down Menu)</div>
  <div class="field" style="left:44px;top:102px;width:82px;height:34px">Message</div>
  <div class="field" style="left:44px;top:138px;width:39px;height:10px">Captcha Field</div>
  <span class="btn abs" style="left:44px;top:151px">Submit</span>
  <div class="abs" style="left:130px;top:67px;width:40px;height:69px;background:linear-gradient(160deg,#d7e6d2,#c9d9e3)" role="img" aria-label="Street map of the clinic location"></div>
  <p class="abs" style="left:140px;top:138px;font-size:1.9px;color:#333">Address</p>
  <footer class="footer">
    <ul class="links"><li>About</li><li>Fertility &amp; Pregnancy</li><li>Hormone Balance</li><li>Strength &amp; Structure</li><li>Emotional Wellbeing</li><li>Online Shop</li><li>Testimonials</li></ul>
    <div class="contact"><p>Contact:</p><p>555-014-2290</p><p>info@willowgate.com</p></div>
    <div class="social"><span></span><span></span><span></span><span></span></div>
    <div class="brand"><div class="mark"></div><div class="name">Willowgate</div></div>
    <p class="copy">Copyright @ 2021 Willowgate All Rights Reserved</p>
  </footer>
</section>

</body>
</html>
```